Banner Ad Design Project

I need a nice banner ad for my company. I do IT development and IT Consulting. The banner should contain my company Logo (see my website www.bramtor-lune.net) and should use the colors from my website (www.bramtor-lune.net). The final design should communicate trust, creativity and competence. It would by nice, when the banner has some animation effects.

Target Market(s)

Manager, IT Directors, IT Decider, HR Manager, Business People

Industry/Entity Type

It Company

Requirements
Must have
• Use my company logo
Use my colors from my website
Technology oriented
Serious but not boring
Some animation
Should not have
• Sound

```html
<!DOCTYPE html>
<html lang="en">
<head>
<meta charset="utf-8">
<title>Bramtor Lune – Banner Set</title>
<link rel="stylesheet" href="https://fonts.googleapis.com/css2?family=Exo+2:wght@700&family=Open+Sans:wght@600&display=swap">
<style>
  :root {
    --page-light: #f4f6f7;
    --page-shade: #cdd5d9;
    --accent-yellow: #f2d600;
    --brand-gold: #e3b000;
    --headline: #e9ecee;
    --headline-shade: #9aa0a4;
    --copy: #ffffff;
    --screen-glow: #8fa4b8;
    --screen-dark: #1b2430;
  }
  * { box-sizing: border-box; margin: 0; padding: 0; }
  html, body { width: 1185px; height: 1200px; overflow: hidden; }
  body {
    position: relative;
    background: radial-gradient(ellipse at 50% 45%, var(--page-light) 0%, #e6eaec 55%, var(--page-shade) 100%);
    font-family: "Open Sans", Arial, sans-serif;
  }
  .banner {
    position: absolute;
    left: 112px;
    width: 985px;
    height: 126px;
    overflow: hidden;
    box-shadow: 0 2px 6px rgba(0,0,0,0.18);
  }
  .banner-bg { position: absolute; inset: 0; width: 100%; height: 100%; }
  .monitor-art {
    position: absolute;
    left: 20px;
    top: 6px;
    width: 150px;
    height: 114px;
    border-radius: 6px;
    background: radial-gradient(ellipse at 50% 40%, var(--screen-glow) 0%, var(--screen-dark) 55%, transparent 80%);
  }
  .headline {
    position: absolute;
    left: 250px;
    width: 360px;
    top: 0;
    height: 126px;
    display: flex;
    align-items: center;
    justify-content: center;
    font-family: "Exo 2", Arial, sans-serif;
    font-weight: 700;
    font-size: 50px;
    letter-spacing: 1px;
    color: var(--headline);
    background: linear-gradient(180deg, #ffffff 0%, var(--headline) 50%, var(--headline-shade) 100%);
    -webkit-background-clip: text;
    background-clip: text;
    -webkit-text-fill-color: transparent;
    filter: drop-shadow(0 3px 2px rgba(0,0,0,0.8));
  }
  .headline.is-caps { font-size: 52px; letter-spacing: 2px; }
  .service-list {
    position: absolute;
    left: 230px;
    width: 400px;
    top: 8px;
    list-style: none;
    text-align: center;
    color: var(--copy);
    font-weight: 600;
    font-size: 27px;
    line-height: 40px;
  }
  .service-list.is-three { top: 2px; }
  .brand {
    position: absolute;
    left: 760px;
    top: 0;
    width: 210px;
    height: 126px;
  }
  .brand-dot {
    position: absolute;
    left: 92px;
    top: 22px;
    width: 30px;
    height: 30px;
    border-radius: 50%;
    background: var(--brand-gold);
  }
  .brand-name {
    position: absolute;
    left: 0;
    right: 0;
    top: 78px;
    text-align: center;
    font-weight: 600;
    font-size: 23px;
    color: var(--brand-gold);
  }
</style>
</head>
<body>

<svg width="0" height="0" style="position:absolute" aria-hidden="true">
  <defs>
    <linearGradient id="dark-fill" x1="0" y1="0" x2="1" y2="1">
      <stop offset="0" stop-color="#000"/>
      <stop offset="0.45" stop-color="#2a2a2a"/>
      <stop offset="1" stop-color="#0c0c0c"/>
    </linearGradient>
    <symbol id="banner-shape" viewBox="0 0 985 126" preserveAspectRatio="none">
      <rect width="985" height="126" fill="#ffffff"/>
      <path d="M0 0 H715 C700 55 670 100 612 126 H0 Z" fill="url(#dark-fill)"/>
      <path d="M715 0 H750 C735 60 705 105 650 126 H612 C670 100 700 55 715 0 Z" fill="#f2d600"/>
    </symbol>
  </defs>
</svg>

<section class="banner" style="top:130px">
  <svg class="banner-bg"><use href="#banner-shape"/></svg>
  <div class="monitor-art" role="img" aria-label="Glowing flat-screen monitor"></div>
  <div class="headline">Technology</div>
  <div class="brand"><span class="brand-dot"></span><span class="brand-name">bramtor-lune.net</span></div>
</section>

<section class="banner" style="top:290px">
  <svg class="banner-bg"><use href="#banner-shape"/></svg>
  <div class="monitor-art" role="img" aria-label="Glowing flat-screen monitor"></div>
  <div class="headline">Development</div>
  <div class="brand"><span class="brand-dot"></span><span class="brand-name">bramtor-lune.net</span></div>
</section>

<section class="banner" style="top:450px">
  <svg class="banner-bg"><use href="#banner-shape"/></svg>
  <div class="monitor-art" role="img" aria-label="Glowing flat-screen monitor"></div>
  <div class="headline is-caps">SUCCES</div>
  <div class="brand"><span class="brand-dot"></span><span class="brand-name">bramtor-lune.net</span></div>
</section>

<section class="banner" style="top:612px">
  <svg class="banner-bg"><use href="#banner-shape"/></svg>
  <div class="monitor-art" role="img" aria-label="Glowing flat-screen monitor"></div>
  <ul class="service-list">
    <li>DeskPortal Consultiong</li>
  </ul>
  <div class="brand"><span class="brand-dot"></span><span class="brand-name">bramtor-lune.net</span></div>
</section>

<section class="banner" style="top:775px">
  <svg class="banner-bg"><use href="#banner-shape"/></svg>
  <div class="monitor-art" role="img" aria-label="Glowing flat-screen monitor"></div>
  <ul class="service-list">
    <li>DeskPortal Consultiong</li>
    <li>.NOVA Technology</li>
  </ul>
  <div class="brand"><span class="brand-dot"></span><span class="brand-name">bramtor-lune.net</span></div>
</section>

<section class="banner" style="top:941px">
  <svg class="banner-bg"><use href="#banner-shape"/></svg>
  <div class="monitor-art" role="img" aria-label="Glowing flat-screen monitor"></div>
  <ul class="service-list is-three">
    <li>DeskPortal Consultiong</li>
    <li>.NOVA Technology</li>
    <li>Software Development</li>
  </ul>
  <div class="brand"><span class="brand-dot"></span><span class="brand-name">bramtor-lune.net</span></div>
</section>

</body>
</html>
```